Business cards Dör Kornhüüs GmbH & Co.KG

We need a uniform business card design template for our employees.
A template should be created to have the same design for all business cards.

Contact Information for Business Card

Firma und Firmierung, Name, Funktion in Unternehmen, Anschrift, Tel. Handynummer, Emailadresse, Internetseite

Colors

Designer to choose colors to be used in the design.

Requirements
Must have
• Our company logo must be on it

```html
<!DOCTYPE html>
<html lang="de">
<head>
<meta charset="utf-8">
<title>Dör Kornhüüs – Visitenkarte</title>
<link href="https://fonts.googleapis.com/css2?family=Lato:wght@400;700&family=Tinos:wght@700&display=swap" rel="stylesheet">
<style>
  :root {
    --backdrop: #1f1f1f;
    --paper: #ffffff;
    --rose: #f07080;
    --rose-deep: #ee5f78;
    --lilac: #c49ac8;
    --ink: #1c1c1c;
    --blush: #fbd3d8;
  }
  * { margin: 0; padding: 0; box-sizing: border-box; }
  html, body { width: 1200px; height: 900px; overflow: hidden; }
  body {
    position: relative;
    background: var(--backdrop);
    font-family: "Lato", Arial, sans-serif;
  }
  .card {
    position: absolute;
    top: 200px;
    width: 310px;
    height: 502px;
    box-shadow: 4px 5px 6px rgba(0,0,0,0.55);
  }
  .card--front {
    left: 253px;
    background: var(--paper);
    border-radius: 62px 0 62px 0;
  }
  .card--back {
    left: 627px;
    background: var(--rose);
    border-radius: 0 62px 0 62px;
  }
  .brand {
    position: absolute;
    left: 0;
    right: 0;
    text-align: center;
  }
  .card--front .brand { top: 126px; }
  .card--back .brand { top: 226px; }
  .brand__name {
    font-family: "Lato", Arial, sans-serif;
    font-weight: 700;
    font-size: 30px;
    letter-spacing: 1px;
    line-height: 1.1;
  }
  .brand__tagline {
    font-family: "Lato", Arial, sans-serif;
    font-weight: 400;
    font-size: 13px;
    letter-spacing: 2.6px;
    margin-top: 4px;
  }
  .card--front .brand__name { color: var(--rose-deep); }
  .card--front .brand__tagline { color: var(--lilac); }
  .card--back .brand__name { color: var(--blush); }
  .card--back .brand__tagline { color: var(--blush); }

  .contact {
    position: absolute;
    left: 33px;
    top: 328px;
    color: var(--ink);
    font-size: 14.5px;
  }
  .contact__name {
    font-family: "Tinos", "Times New Roman", serif;
    font-weight: 700;
    font-size: 17.5px;
    color: var(--rose-deep);
    line-height: 1.1;
  }
  .contact__role { line-height: 1.2; margin-bottom: 6px; }
  .contact__line {
    display: flex;
    align-items: center;
    gap: 4px;
    height: 19.5px;
  }
  .contact__line svg { width: 13px; height: 13px; flex: none; }
  .contact__address { margin-top: 7px; line-height: 1.25; }
  .card__web {
    position: absolute;
    left: 0;
    right: 0;
    top: 444px;
    text-align: center;
    color: var(--paper);
    font-size: 13.5px;
    font-weight: 700;
  }
</style>
</head>
<body>
  <section class="card card--front" aria-label="Vorderseite">
    <div class="brand">
      <div class="brand__name">Dör Kornhüüs</div>
      <div class="brand__tagline">Nordische Backkunst</div>
    </div>
    <div class="contact">
      <div class="contact__name">JONAS HARTWIG</div>
      <div class="contact__role">Managing Director</div>
      <div class="contact__line">
        <svg viewBox="0 0 16 16" aria-hidden="true"><path fill="var(--rose)" d="M2 5c0-2 3-3 6-3s6 1 6 3v1h-3V5H5v1H2zM4 7h8l2 6H2zm4 1.5a2 2 0 1 0 0 4 2 2 0 0 0 0-4z"/></svg>
        <span>044-123 456 789</span>
      </div>
      <div class="contact__line">
        <svg viewBox="0 0 16 16" aria-hidden="true"><rect x="1" y="3" width="14" height="10" fill="var(--rose)"/><path d="M1.5 3.5 8 9l6.5-5.5" fill="none" stroke="#fff" stroke-width="1.3"/></svg>
        <span>info@webname.com</span>
      </div>
      <div class="contact__line">
        <svg viewBox="0 0 16 16" aria-hidden="true"><circle cx="8" cy="8" r="7" fill="var(--rose)"/><path d="M4 5c2 0 2 2 4 2s1 3 3 3M9 3c0 2 2 2 3 2" fill="none" stroke="#fff" stroke-width="1.3"/></svg>
        <span>www.websitename.com</span>
      </div>
      <div class="contact__address">421, Address line here<br>Country Name, 45452</div>
    </div>
  </section>

  <section class="card card--back" aria-label="Rückseite">
    <div class="brand">
      <div class="brand__name">Dör Kornhüüs</div>
      <div class="brand__tagline">Nordische Backkunst</div>
    </div>
    <div class="card__web">www.websitename.com</div>
  </section>
</body>
</html>
```